Need professional looking PowerPoint Slide

Content is all created but it looks lame. I need it to look good. Please modify attached slide. Logo needs to stay on it. Green color should be used as well.
Industry/Entity Type
Health Care
Font styles to use
Serif
Requirements
Must have
- all original content contained
Nice to have
- additional design elements such as photo(s)

```html
<!DOCTYPE html>
<html lang="en">
<head>
<meta charset="utf-8">
<title>Innovation Stages to a New Care Model</title>
<link href="https://fonts.googleapis.com/css2?family=Carlito:wght@400;700&display=swap" rel="stylesheet">
<style>
  :root {
    --green: #4f8a30;
    --grey-text: #7a7a7a;
    --frame: #d4d4d4;
    --swoosh: #e6e6e6;
    --white: #ffffff;
  }
  html, body {
    margin: 0;
    padding: 0;
    width: 1200px;
    height: 972px;
    overflow: hidden;
    background: var(--white);
  }
  .canvas {
    position: relative;
    width: 1100px;
    height: 891px;
    transform: scale(1.0909);
    transform-origin: 0 0;
    font-family: "Carlito", sans-serif;
  }
  .slide {
    position: absolute;
    left: 18px;
    top: 45px;
    width: 1064px;
    height: 800px;
    background: var(--white);
    border: 1px solid var(--frame);
    box-shadow: 3px 3px 6px rgba(0,0,0,0.18);
    overflow: hidden;
  }
  .art { position: absolute; left: 0; top: 0; }
  .goals-label {
    position: absolute;
    left: 35px;
    top: 58px;
    margin: 0;
    font-size: 28px;
    font-weight: 700;
    color: var(--green);
  }
  .goals {
    position: absolute;
    left: 127px;
    top: 26px;
    color: var(--grey-text);
    font-size: 20px;
    line-height: 25px;
    letter-spacing: 0.9px;
  }
  .goals p { margin: 0; }
  .goals ul, .column ul { margin: 0; padding: 0; list-style: none; }
  .goals li, .column li { position: relative; padding-left: 27px; }
  .goals li::before, .column li::before {
    content: "•";
    position: absolute;
    left: 2px;
    color: var(--green);
  }
  .stage-title {
    position: absolute;
    left: 114px;
    top: 296px;
    margin: 0;
    font-size: 48px;
    line-height: 58px;
    font-weight: 700;
    color: var(--green);
  }
  .stage-title span { display: block; }
  .stage-title span + span { padding-left: 64px; }
  .column {
    position: absolute;
    top: 580px;
    color: var(--grey-text);
    font-size: 17px;
    line-height: 21.5px;
    letter-spacing: 0.5px;
  }
  .column h3 {
    margin: 0 0 10px;
    font-size: 17px;
    font-weight: 700;
    letter-spacing: 0;
    color: var(--green);
  }
  .column li { padding-left: 20px; }
  .col-tech { left: 52px; width: 165px; }
  .col-value { left: 260px; width: 245px; }
  .col-business { left: 540px; width: 250px; }
  .col-service { left: 818px; width: 180px; }
  .footer-title {
    position: absolute;
    left: 0;
    width: 1060px;
    top: 752px;
    margin: 0;
    text-align: center;
    font-size: 30px;
    font-weight: 700;
    color: var(--green);
  }
  .brand-name {
    position: absolute;
    left: 890px;
    top: 748px;
    font-size: 26px;
    font-weight: 700;
    color: var(--green);
    line-height: 1;
  }
</style>
</head>
<body>
<div class="canvas">
  <section class="slide">
    <svg class="art" width="1064" height="800" viewBox="18 45 1064 800" aria-hidden="true">
      <path d="M18 800 C 300 780, 700 770, 1082 762 L1082 845 L18 845 Z" fill="var(--swoosh)"/>
      <path d="M18 806 C 300 790, 700 780, 1082 772 L1082 845 L18 845 Z" fill="var(--white)"/>
      <g fill="var(--green)">
        <circle cx="760" cy="332" r="145"/>
        <circle cx="684" cy="458" r="152"/>
        <circle cx="840" cy="462" r="148"/>
      </g>
      <circle cx="759" cy="404" r="78" fill="var(--white)"/>
      <g fill="none" stroke="var(--white)" stroke-width="6">
        <circle cx="760" cy="332" r="145"/>
        <circle cx="684" cy="458" r="152"/>
        <circle cx="840" cy="462" r="148"/>
      </g>
      <g font-family="Carlito, sans-serif" fill="var(--white)">
        <text x="760" y="223" font-size="22" font-weight="700" text-anchor="middle">Research</text>
        <text x="704" y="265" font-size="14">• Market study</text>
        <text x="638" y="288" font-size="14">• Macro issues</text>
        <text x="778" y="288" font-size="14">• Data Analytics</text>
        <text x="546" y="466" font-size="22" font-weight="700">Exploration</text>
        <text x="548" y="502" font-size="14">• Solution proposal</text>
        <text x="561" y="529" font-size="14">• Ethnography</text>
        <text x="858" y="466" font-size="22" font-weight="700">Execution</text>
        <text x="858" y="502" font-size="14">• Service</text>
        <text x="871" y="521" font-size="14">creation</text>
        <text x="839" y="547" font-size="14">• Verification</text>
        <text x="825" y="574" font-size="14">• Validation</text>
      </g>
      <g font-family="Carlito, sans-serif" fill="var(--green)" font-size="22" font-weight="700" text-anchor="middle">
        <text x="757" y="385">New</text>
        <text x="757" y="413">Service</text>
        <text x="757" y="441">Launch</text>
      </g>
    </svg>

    <h2 class="goals-label">Goals</h2>
    <div class="goals">
      <p>Assist in Renewing/Redefining your Value Proposition:</p>
      <ul>
        <li>Change your healthcare delivery model</li>
        <li>Redefine the way you engage with patients/families</li>
        <li>Take new steps in achieving the Triple-Aim plus One</li>
      </ul>
    </div>

    <h1 class="stage-title"><span>Stages to a New</span><span>Care Model</span></h1>

    <div class="column col-tech">
      <h3>New Technology</h3>
      <ul>
        <li>Smartphone and tablet apps</li>
        <li>EMR</li>
        <li>3T MRI</li>
        <li>Virtual visits</li>
        <li>Telehealth</li>
      </ul>
    </div>
    <div class="column col-value">
      <h3>New Value Proposition</h3>
      <ul>
        <li>Population Health</li>
        <li>Redesign continuum of care from fee-for-service based model to at-risk</li>
        <li>Bundled Payment</li>
      </ul>
    </div>
    <div class="column col-business">
      <h3>New Business Model</h3>
      <ul>
        <li>Hub &amp; Spoke</li>
        <li>Extend from Ambulatory to Integrated System</li>
        <li>Health plans</li>
      </ul>
    </div>
    <div class="column col-service">
      <h3>New Service Line</h3>
      <ul>
        <li>Orthopedics</li>
        <li>Oncology</li>
        <li>Cardiology</li>
      </ul>
    </div>

    <h2 class="footer-title">Innovation Stages to a New Care Model</h2>
    <div class="brand-name">Verdant</div>
  </section>
</div>
</body>
</html>
```